Contemporary Elegant Business Card Design for an International Trade Company in the Wine Industry

We need a new business card design for an international trade company in the wine and winemaking industry. The overall feel of the card should be contemporary, upscale, luxurious and elegant. It should communicate confidence and professionalism. The colors should complementary to our logo design (burgundy, gold, and black).
Inspiration: rich velvet tapestry
The card should include the following information:
Business: Brovenna Trading/Shipping, LLC.
Name: Marcus T. Hollenbrand
Title: CEO
Email: mark@brovennatrading.example
Phone: 555-294-6172
www.brovennatrading.example
Updates
Project Deadline Extended
Reason: We'd like the designers that we requested some additional designs from to still submit designs. Thank you!
Industry/Entity Type
Business
Contact Information for Business Card
Title: CEO
Phone: 555-294-6172
www.brovennatrading.example
Look and feel

```html
<!DOCTYPE html>
<html lang="en">
<head>
<meta charset="utf-8">
<title>Brovenna Trading/Shipping — Business Cards</title>
<link rel="stylesheet" href="https://fonts.googleapis.com/css2?family=Open+Sans:wght@400;600;700&display=swap">
<style>
  :root {
    --backdrop: #2b2522;
    --card-black: #0c0c0c;
    --burgundy: #7e1a22;
    --gold: #e0a02e;
    --text-light: #e2e2e2;
    --text-muted: #a8a8a8;
  }
  * { margin: 0; padding: 0; box-sizing: border-box; }
  html, body {
    width: 1200px;
    height: 768px;
    overflow: hidden;
    background: var(--backdrop);
    font-family: "Open Sans", Arial, sans-serif;
  }
  .stage {
    position: relative;
    width: 1200px;
    height: 768px;
  }
  .business-card {
    position: absolute;
    top: 224px;
    width: 560px;
    height: 320px;
    background: var(--card-black);
    box-shadow: 0 14px 32px rgba(0,0,0,0.5);
  }
  .card-front { left: 26px; }
  .card-back { left: 614px; }

  .brand-square {
    position: absolute;
    background: var(--burgundy);
  }
  .brand-name {
    position: absolute;
    color: var(--text-light);
    font-weight: 700;
    line-height: 1.15;
  }

  .card-front .brand-square {
    left: 205px;
    top: 48px;
    width: 150px;
    height: 150px;
  }
  .card-front .brand-name {
    left: 130px;
    top: 210px;
    width: 300px;
    text-align: center;
    font-size: 22px;
  }

  .card-back .brand-square {
    left: 70px;
    top: 60px;
    width: 140px;
    height: 140px;
  }
  .card-back .brand-name {
    left: 50px;
    top: 210px;
    width: 180px;
    text-align: center;
    font-size: 17px;
  }

  .contact-block {
    position: absolute;
    left: 290px;
    top: 138px;
  }
  .person-name {
    color: var(--gold);
    font-weight: 600;
    font-size: 18px;
    line-height: 1.2;
  }
  .person-title {
    color: var(--text-muted);
    font-size: 11px;
    margin-top: 3px;
  }
  .contact-list {
    list-style: none;
    margin-top: 22px;
  }
  .contact-list li {
    display: flex;
    align-items: center;
    gap: 10px;
    color: var(--text-light);
    font-size: 13px;
    line-height: 1.65;
  }
  .contact-icon {
    width: 11px;
    height: 11px;
    flex: none;
    fill: var(--gold);
  }
</style>
</head>
<body>
<main class="stage">
  <section class="business-card card-front">
    <span class="brand-square"></span>
    <span class="brand-name">Brovenna Trading/Shipping, LLC.</span>
  </section>

  <section class="business-card card-back">
    <span class="brand-square"></span>
    <span class="brand-name">Brovenna Trading/Shipping, LLC.</span>

    <div class="contact-block">
      <h1 class="person-name">Marcus T. Hollenbrand</h1>
      <p class="person-title">CEO</p>
      <ul class="contact-list">
        <li>
          <svg class="contact-icon" viewBox="0 0 20 20" aria-hidden="true">
            <path d="M4 3h3l2 4-2 1.5a10 10 0 0 0 4.5 4.5L13 11l4 2v3a2 2 0 0 1-2 2C8.5 18 2 11.5 2 5a2 2 0 0 1 2-2z"/>
          </svg>
          <span>555-294-6172</span>
        </li>
        <li>
          <svg class="contact-icon" viewBox="0 0 20 20" aria-hidden="true">
            <path d="M2 4h16v12H2z M3 5l7 6 7-6" stroke="#0c0c0c" stroke-width="1.2"/>
          </svg>
          <span>mark@brovennatrading.example</span>
        </li>
        <li>
          <svg class="contact-icon" viewBox="0 0 20 20" aria-hidden="true">
            <circle cx="10" cy="10" r="8"/>
            <path d="M2 10h16 M10 2c-3 3-3 13 0 16 M10 2c3 3 3 13 0 16" stroke="#0c0c0c" stroke-width="1.2" fill="none"/>
          </svg>
          <span>www.brovennatrading.example</span>
        </li>
      </ul>
    </div>
  </section>
</main>
</body>
</html>
```